Modern and strong website design for a Dutch crowdsourcing company
.

We are startup company providing crowdsourcing of administrative and customers service tasks for larger companies and other organizations. We offer cost savings and scale-ability combined with higher quality of execution. We will soon enter the market and need a website that has two major target groups: 1. Our corporate customers 2. The mainly younger crowd executing the tasks on our platform.
The target group of customers are Influencers and decision makers with companies and other organizations in with large administrative and customer service departments. Most information in the startup phase will be targeting this group.
The target group of future crowd workers will be heterogeneous, from students to stay at home mums or night shift workers who want to earn some extra money by performing easy to execute microtasks in the cloud. We will target both Dutch and international workers.

The website must be developed for browsing on a computer but also be optimized for mobile devices and tablets.
The website must be optimized and tested for the major browsers on windows, macOS and mobile devices.

For the minimum requirement for the website see attached wireframes

The present landing page http://thepinegladeloft.com and logo are not reflecting our preferences!
See enclosed a new logo that stands for both the crowdwork (performed for our customers) and the crowd (the pine glade loft).

Target Market(s)

see tekst above.

Industry/Entity Type

Business Service

Coding

Coded - Design and coding required

Number of Pages Required

5+ page

Font styles to use
Sans Serif
Other font styles liked:
• Lato, Open Sans

Colors

Designer to choose colors to be used in the design.

Requirements
Must have
• start devider screen
• home page displaying business and worker information
• a page displaying only info for businesses
• a page displaying only info for workers
• a contact form
• a reviews page
• color scheme from logo
• responsiveness!
Nice to have
• Nice animations
• overlapping blocks, animated on scroll
• lightbox effects if applicable
• animated mobile menu icon and menu itself

```html
<!DOCTYPE html>
<html lang="en">
<head>
<meta charset="utf-8">
<title>The Pine Glade Loft</title>
<link href="https://fonts.googleapis.com/css2?family=Poppins:wght@600;700&family=Montserrat:wght@400;500&display=swap" rel="stylesheet">
<style>
  :root {
    --black: #000000;
    --orange: #e07800;
    --orange-bright: #f07f00;
    --cream: #f8f1ec;
    --ink: #222222;
    --white: #ffffff;
    --hero-dark: #2b2b2d;
  }
  * { margin: 0; padding: 0; box-sizing: border-box; }
  html, body { width: 927px; height: 1200px; overflow: hidden; }
  body {
    position: relative;
    font-family: "Montserrat", Arial, sans-serif;
    background: var(--white);
    color: var(--ink);
  }
  .site-header {
    position: absolute; left: 0; top: 0; width: 927px; height: 75px;
    background: var(--black);
  }
  .brand {
    position: absolute; left: 66px; top: 19px; width: 110px;
    font-family: "Poppins", sans-serif; font-weight: 600; font-size: 15px; line-height: 18px;
    color: var(--orange-bright);
  }
  .main-nav { position: absolute; top: 32px; left: 198px; display: flex; gap: 32px; }
  .main-nav a, .footer-nav a {
    color: var(--white); text-decoration: none; font-size: 10.6px; text-transform: uppercase;
  }
  .cta {
    position: absolute; left: 736px; top: 24px; width: 125px; height: 28px;
    background: var(--orange-bright); color: var(--white);
    font-size: 9.4px; font-weight: 500; text-transform: uppercase;
    display: flex; align-items: center; justify-content: center; text-decoration: none;
  }
  .hero {
    position: absolute; left: 0; top: 75px; width: 927px; height: 355px;
    background: radial-gradient(ellipse at 50% 40%, #4a4a4e 0%, var(--hero-dark) 60%, #1c1c1e 100%);
  }
  .hero-name {
    position: absolute; left: 0; top: 82px; width: 927px; text-align: center;
    font-family: "Poppins", sans-serif; font-weight: 700; font-size: 46px; line-height: 50px;
    color: var(--orange-bright);
  }
  .hero-tagline {
    position: absolute; left: 263px; top: 199px; width: 400px; text-align: center;
    color: var(--white); font-size: 14px; line-height: 23px;
  }
  .section { position: absolute; left: 0; width: 927px; }
  .business { top: 430px; height: 355px; background: var(--cream); }
  .workers { top: 785px; height: 353px; background: var(--orange); }
  .photo-frame {
    position: absolute; width: 290px; height: 243px; background: var(--white); padding: 5px;
    box-shadow: 0 1px 6px rgba(0,0,0,0.25);
  }
  .photo { width: 100%; height: 100%; }
  .photo-handshake { background: linear-gradient(135deg, #5d7fae 0%, #9db4cf 45%, #3c4d68 100%); }
  .photo-gloves { background: linear-gradient(135deg, #e9c08a 0%, #f2dcc2 45%, #c8866c 100%); }
  .section-title {
    position: absolute; font-family: "Poppins", sans-serif; font-weight: 700;
    font-size: 39px; line-height: 44px;
  }
  .business .section-title { left: 398px; top: 56px; color: var(--orange); }
  .workers .section-title { left: 66px; top: 60px; color: var(--white); }
  .section-copy { position: absolute; width: 460px; font-size: 9.9px; line-height: 15.6px; }
  .section-copy p + p { margin-top: 15.6px; }
  .business .section-copy { left: 401px; top: 114px; color: var(--ink); }
  .workers .section-copy { left: 68px; top: 113px; color: var(--white); }
  .site-footer {
    position: absolute; left: 0; top: 1138px; width: 927px; height: 62px; background: var(--black);
    font-size: 10.4px;
  }
  .contact-line {
    position: absolute; top: 24px; display: flex; align-items: center; gap: 6px;
    color: var(--orange-bright);
  }
  .contact-email { left: 68px; }
  .contact-phone { left: 254px; }
  .footer-nav { position: absolute; left: 362px; top: 25px; display: flex; gap: 9px; color: var(--white); }
  .footer-nav a { font-size: 9.4px; }
  .copyright { position: absolute; right: 67px; top: 24px; color: var(--white); }
</style>
</head>
<body>
  <header class="site-header">
    <div class="brand">The Pine<br>Glade Loft</div>
    <nav class="main-nav">
      <a href="#">Home</a>
      <a href="#">For Businesses</a>
      <a href="#">For Workers</a>
    </nav>
    <a class="cta" href="#">Get in contact</a>
  </header>

  <section class="hero" role="img" aria-label="Photo of people working together in a busy office">
    <div class="hero-name">The Pine<br>Glade Loft</div>
    <p class="hero-tagline">Lorem Ipsum is simply dummy text of the printing and typesetting industry. Lorem Ipsum</p>
  </section>

  <section class="section business">
    <div class="photo-frame" style="left:68px; top:56px;">
      <div class="photo photo-handshake" role="img" aria-label="Photo of a business handshake in front of a city skyline"></div>
    </div>
    <h2 class="section-title">For Businesses</h2>
    <div class="section-copy">
      <p>Lorem Ipsum is simply dummy text of the printing and typesetting industry. Lorem Ipsum has been the industry's standard dummy text ever since the 1500s, when an unknown printer took a galley of type and scrambled it to make a type specimen book. It has survived not only five centuries, but also the leap into electronic typesetting, remaining essentially unchanged. It was popularised in the 1960s with the release of Lettersheet sheets containing Lorem Ipsum passages, and more recently with desktop publishing software like Pagecraft Studio including versions of Lorem Ipsum.</p>
      <p>Lorem Ipsum is simply dummy text of the printing and typesetting industry. Lorem Ipsum has been the industry's standard dummy text ever since the 1500s, when an unknown printer took a galley of type and scrambled it to make a type specimen book.</p>
    </div>
  </section>

  <section class="section workers">
    <h2 class="section-title">For Crowd Workers</h2>
    <div class="section-copy">
      <p>Lorem Ipsum is simply dummy text of the printing and typesetting industry. Lorem Ipsum has been the industry's standard dummy text ever since the 1500s, when an unknown printer took a galley of type and scrambled it to make a type specimen book. It has survived not only five centuries, but also the leap into electronic typesetting, remaining essentially unchanged. It was popularised in the 1960s with the release of Lettersheet sheets containing Lorem Ipsum passages, and more recently with desktop publishing software like Pagecraft Studio including versions of Lorem Ipsum.</p>
      <p>Lorem Ipsum is simply dummy text of the printing and typesetting industry. Lorem Ipsum has been the industry's standard dummy text ever since the 1500s, when an unknown printer took a galley of type and scrambled it to make a type specimen book.</p>
    </div>
    <div class="photo-frame" style="left:571px; top:56px;">
      <div class="photo photo-gloves" role="img" aria-label="Photo of two workers in gloves clasping hands"></div>
    </div>
  </section>

  <footer class="site-footer">
    <div class="contact-line contact-email">
      <svg width="10" height="8" viewBox="0 0 10 8" aria-hidden="true"><rect x="0" y="0" width="10" height="8" fill="#f07f00"/><path d="M0 0 L5 4.5 L10 0" fill="none" stroke="#000" stroke-width="1"/></svg>
      <span>info@thepinegladeloft.com</span>
    </div>
    <div class="contact-line contact-phone">
      <svg width="9" height="9" viewBox="0 0 24 24" aria-hidden="true"><path fill="#f07f00" d="M6.6 10.8a15.1 15.1 0 0 0 6.6 6.6l2.2-2.2a1 1 0 0 1 1-.25 11.4 11.4 0 0 0 3.6.57 1 1 0 0 1 1 1V20a1 1 0 0 1-1 1A17 17 0 0 1 3 4a1 1 0 0 1 1-1h3.5a1 1 0 0 1 1 1c0 1.25.2 2.45.57 3.57a1 1 0 0 1-.25 1z"/></svg>
      <span>0698765432</span>
    </div>
    <nav class="footer-nav">
      <a href="#">Home</a><span>|</span><a href="#">For Businesses</a><span>|</span><a href="#">For Workers</a>
    </nav>
    <div class="copyright">Copyright © 2017. The Pine Glade Loft.</div>
  </footer>
</body>
</html>
```